依頼詳細
依頼するページ
・トップページ
・コンセプトページ

清潔感があり、気軽に受講できる雰囲気を出しつつ、赤系を混ぜることで東北をITで盛り上げる熱意を伝えられるデザインを希望します。

提案頂いたデザインをもとに以下のページも作成していきます。
(継続依頼にするか、自社デザインにするかは検討中)
・講座の個別ページ
・開講中の講座一覧のページ
・問い合わせ
・東北地方のITについて紹介するページ(ブログ形式)

グローバルメニューを設置する想定でデザインをお願いします。
サイトURL
ページ数
2ページ
希望イメージ
シンプル 複雑
単色 カラフル
暗い 明るい
日常 高級
遊び心 厳粛
未来的 伝統的
女性的 男性的
希望する色
白、赤
納品ファイル
• イラストレーター形式 (.ai)
• PNG形式 (.png)
補足説明
お二人の方からご提案頂きました。
ありがとうございます。

お二人のご提案を拝見して追記させて頂きます。
コメントすることは大変恐縮なのですが、もう少し東北らしさや、東北を盛り上げることをアピールしたデザインでご提案頂ければと思います。

締め切りも3日ほど延ばさせて頂きました。

宜しくお願い致します。
皆様のご提案大変興味深く拝見しております。ありがとうございます。
社内で意見を集めた結果、もう少し提案を見てみたい、との意見が多く期限を延期する事と致しました。
修正がある方はこの機会にご提案頂けますと、大変嬉しく思います。
それでは宜しくお願い致します。

シンプルでありながら想いの伝わるデザインでした。

みなさんのご提案一つ一つがとてもクオリティが高く、悩みました。ありがとうございました。

```html
<!DOCTYPE html>
<html lang="ja">
<head>
<meta charset="utf-8">
<title>北国ITアカデミー | 北国ITアカデミーとは？</title>
<link rel="stylesheet" href="https://fonts.googleapis.com/css2?family=Noto+Sans+JP:wght@400;500;700&display=swap">
<style>
:root{
  --accent:#f0566a;
  --ink:#333333;
  --text:#555555;
  --muted:#777777;
  --page:#ededed;
  --panel:#ffffff;
  --soft:#f3f3f3;
  --line:#d4d4d4;
  --footer:#222222;
  --footer-text:#e6e6e6;
}
*{margin:0;padding:0;box-sizing:border-box}
html,body{width:1200px;height:2276px;overflow:hidden}
body{position:relative;background:var(--page);font-family:"Noto Sans JP",sans-serif;color:var(--text)}
.abs{position:absolute}

.top-bar{left:0;top:0;width:1200px;height:10px;background:var(--accent)}
.site-header{left:0;top:10px;width:1200px;height:162px;background:var(--panel);box-shadow:0 2px 4px rgba(0,0,0,.25)}
.brand{left:72px;top:30px;font-size:34px;font-weight:400;color:var(--accent);letter-spacing:1px}
.tagline{left:346px;top:48px;font-size:15px;color:var(--muted)}
.phone-icon{left:822px;top:30px}
.phone-number{left:853px;top:18px;font-size:39px;font-weight:500;color:var(--ink);letter-spacing:1px}
.phone-hours{left:864px;top:67px;font-size:12.5px;color:var(--muted)}
.global-nav{left:55px;top:116px;display:flex}
.global-nav a{display:block;width:181.5px;height:56px;border-left:1px solid var(--line);text-align:center;text-decoration:none;color:var(--text);font-size:15px;line-height:1.15;padding-top:6px}
.global-nav a:last-child{border-right:1px solid var(--line)}
.global-nav small{display:block;font-size:13.5px}

.side-nav{left:72px;top:232px;width:238px;height:176px;background:var(--panel);box-shadow:0 2px 4px rgba(0,0,0,.25);padding:16px 0 0 18px}
.side-nav a{display:block;font-size:19px;font-weight:500;color:var(--ink);text-decoration:none;height:48px}

.content{left:343px;top:232px;width:784px;height:1648px;background:var(--panel);box-shadow:0 2px 4px rgba(0,0,0,.25)}
.section-title{font-size:21px;font-weight:500;color:var(--accent);position:absolute;left:18px}
.body-copy{font-size:14px;line-height:27px;color:var(--text);letter-spacing:.6px}
.intro-copy{left:19px;top:60px;width:400px}
.map-area{left:509px;top:56px;width:210px;height:360px;background:linear-gradient(#f6f6f6,#ececec);border-radius:6px}
.feature{left:17px;width:751px;height:227px;background:var(--soft)}
.feature h3{position:absolute;left:17px;top:10px;font-size:19px;font-weight:500;color:var(--ink)}
.feature p{position:absolute;left:17px;top:42px;width:385px}
.feature .photo{position:absolute;left:437px;top:14px;width:295px;height:198px;background:linear-gradient(90deg,#b9b4b0 0%,#e9e4df 45%,#cfb3a6 70%,#c43a3a 100%);border:1px solid #999}
.checklist{left:17px;top:1068px;width:751px;height:306px;background:var(--soft);list-style:none;padding-top:20px}
.checklist li{display:flex;align-items:center;height:53px;padding-left:22px;font-size:19.5px;font-weight:700;color:var(--text);letter-spacing:.5px}
.checklist svg{margin-right:28px;flex:none}
.cta{left:239px;top:1466px;width:306px;height:83px;background:var(--accent);color:#fff;font-size:29px;font-weight:700;text-align:center;line-height:83px;text-decoration:none;letter-spacing:1px}

.site-footer{left:0;top:1962px;width:1200px;height:314px;background:var(--footer);color:var(--footer-text)}
.footer-col{top:26px;width:236px}
.footer-col h4{font-size:15px;font-weight:700;padding-bottom:4px;border-bottom:2px solid #666;margin-bottom:6px}
.footer-col p{font-size:12.5px;line-height:24px}
.footer-col ul{list-style:none}
.footer-col li{font-size:12.5px;line-height:20px;padding:6px 2px 8px;border-bottom:1px dashed #888}
.social{left:74px;top:218px;display:flex;gap:10px}
.social span{width:36px;height:36px;display:block}
.copyright{left:0;top:292px;width:1200px;text-align:center;font-size:11.5px;color:#ccc}
</style>
</head>
<body>
<div class="abs top-bar"></div>
<header class="abs site-header">
  <div class="abs brand">北国ITアカデミー</div>
  <div class="abs tagline">ITで北国を盛り上げよう！</div>
  <svg class="abs phone-icon" width="30" height="46" viewBox="0 0 30 46" aria-hidden="true"><path d="M10 2 L16 3 L17 13 L12 16 Q10 23 13 31 L19 32 L21 42 L14 44 Q3 36 3 22 Q3 8 10 2Z" fill="#444"/></svg>
  <div class="abs phone-number">03-0000-4821</div>
  <div class="abs phone-hours">お電話でのお問い合わせ 平日10:00〜19:00</div>
  <nav class="abs global-nav">
    <a href="#">トップ<small>Top</small></a>
    <a href="#">北国ITアカデミーとは？<small>Infomation</small></a>
    <a href="#">講座一覧<small>Course</small></a>
    <a href="#">開講中講座<small>Open</small></a>
    <a href="#">北国ITブログ<small>Blog</small></a>
    <a href="#">お問い合わせ<small>Contact</small></a>
  </nav>
</header>

<nav class="abs side-nav">
  <a href="#">北国ITアカデミーとは？</a>
  <a href="#">北国ITアカデミーの特徴</a>
  <a href="#">こんな方にオススメ</a>
</nav>

<main class="abs content">
  <h2 class="section-title" style="top:22px">北国ITアカデミーとは？</h2>
  <p class="abs body-copy intro-copy">この文章はダミーです。文字の大きさ、量、字間、行間等を確認するために入れています。この文章はダミーです。文字の大きさ、量、字間、行間等を確認するために入れています。<br>この文章はダミーです。文字の大きさ、量、字間、行間等を確認するために入れています。この文章はダミーです。文字の大きさ、量、字間、行間等を確認するために入れています。この文章はダミーです。<br>文字の大きさ、量、字間、行間等を確認するために入れこの文章はダミーです。文字の大きさ、量、字間、行間等を確認するために入れています。この文章はダミーです。文字の大きさ、量、字間、行間等を確認するために入れています。この文章はダミーです。</p>
  <div class="abs map-area" role="img" aria-label="北国地方の県境を描いた線画の地図"></div>

  <h2 class="section-title" style="top:436px">北国ITアカデミーの特徴</h2>
  <article class="abs feature" style="top:490px">
    <h3>ダミータイトル</h3>
    <p class="body-copy">この文章はダミーです。文字の大きさ、量、字間、行間等を確認するために入れています。この文章はダミーです。文字の大きさ、量、字間、行間等を確認するために入れています。量、字間、行間等を確認するために入れています。行間等を確認するために入れています。この文章はダミーです。</p>
    <div class="photo" role="img" aria-label="パソコンに向かって受講する女性の写真"></div>
  </article>
  <article class="abs feature" style="top:744px">
    <h3>ダミータイトル</h3>
    <p class="body-copy">この文章はダミーです。文字の大きさ、量、字間、行間等を確認するために入れています。この文章はダミーです。文字の大きさ、量、字間、行間等を確認するために入れています。量、字間、行間等を確認するために入れています。行間等を確認するために入れています。この文章はダミーです。</p>
    <div class="photo" role="img" aria-label="パソコンに向かって受講する女性の写真"></div>
  </article>

  <h2 class="section-title" style="top:1014px">こんな方にオススメ</h2>
  <ul class="abs checklist">
    <li><svg width="36" height="36" viewBox="0 0 36 36" aria-hidden="true"><path d="M3 20 L13 31 L33 4" fill="none" stroke="var(--accent)" stroke-width="6" stroke-linecap="round" stroke-linejoin="round"/></svg>この文章はダミーです。文字の大きさ、量、字間、行間等を確認す</li>
    <li><svg width="36" height="36" viewBox="0 0 36 36" aria-hidden="true"><path d="M3 20 L13 31 L33 4" fill="none" stroke="var(--accent)" stroke-width="6" stroke-linecap="round" stroke-linejoin="round"/></svg>この文章はダミーです。文字の大きさ、量、字間、行間等を確認す</li>
    <li><svg width="36" height="36" viewBox="0 0 36 36" aria-hidden="true"><path d="M3 20 L13 31 L33 4" fill="none" stroke="var(--accent)" stroke-width="6" stroke-linecap="round" stroke-linejoin="round"/></svg>この文章はダミーです。文字の大きさ、量、字間、行間等を確認す</li>
    <li><svg width="36" height="36" viewBox="0 0 36 36" aria-hidden="true"><path d="M3 20 L13 31 L33 4" fill="none" stroke="var(--accent)" stroke-width="6" stroke-linecap="round" stroke-linejoin="round"/></svg>この文章はダミーです。文字の大きさ、量、字間、行間等を確認す</li>
    <li><svg width="36" height="36" viewBox="0 0 36 36" aria-hidden="true"><path d="M3 20 L13 31 L33 4" fill="none" stroke="var(--accent)" stroke-width="6" stroke-linecap="round" stroke-linejoin="round"/></svg>この文章はダミーです。文字の大きさ、量、字間、行間等を確認す</li>
  </ul>
  <a class="abs cta" href="#">講座一覧を見る</a>
</main>

<footer class="abs site-footer">
  <section class="abs footer-col" style="left:74px">
    <h4>北国ITアカデミー について</h4>
    <p>この文章はダミーです。文字の大きさ、量、字間、行間等を確認するために入れています。この文章はダミーです。文字の大きさ、量、字間、行間等を確認するために入れています。この文章はダミーです。文字の大きさ、</p>
  </section>
  <section class="abs footer-col" style="left:346px">
    <h4>講座一覧</h4>
    <ul>
      <li>趣味からはじめるスマホアプリ<br>作成講座</li>
      <li>はじめてのプログラミング入門</li>
      <li>CMSブログ入門</li>
      <li>HTML5ホームページ作成</li>
    </ul>
  </section>
  <section class="abs footer-col" style="left:618px">
    <h4>北国ITブログ</h4>
    <ul>
      <li>趣味からはじめるスマホアプリ<br>作成講座</li>
      <li>この文章はダミーです。文字の<br>大きさ、量、字間</li>
      <li>この文章はダミーです。文字の<br>大きさ、量、字間</li>
    </ul>
  </section>
  <section class="abs footer-col" style="left:889px">
    <h4>ご利用ガイド</h4>
    <ul>
      <li>よくある質問</li>
      <li>プライバシーポリシー</li>
      <li>特定商取引法</li>
      <li>お問い合わせ</li>
      <li>運営会社</li>
    </ul>
  </section>
  <div class="abs social" aria-label="SNSリンク">
    <span style="background:#3b5a99"></span>
    <span style="background:#2ea3dc"></span>
    <span style="background:#d34836"></span>
    <span style="background:#c8232c"></span>
  </div>
  <div class="abs copyright">copy © 2013 kitaguni-it.example All Right Reserved</div>
</footer>
</body>
</html>
```